Visitenkarten-Design Beratungsunternehmen
Zielgruppe
Beratung, Konzeption, Planung für medizinische Einrichtungen (Arzt- / Zahnarztpraxen)
Zielgruppe: Ärzte / Zahnärzte / Wirtschaftsberater / Planer
https://www.taleron-planwerk.de/
Aufgabenstellung
Klassische Visitenkarte zur allgemeinen Verwendung und Weitergabe.
Das Logo analog der Website, wird dann entsprechend zur Verfügung gestellt.
Kontaktdaten analog der angegebenen Website: https://www.taleron-planwerk.de/

```html
<!DOCTYPE html>
<html lang="de">
<head>
<meta charset="utf-8">
<title>Taleron Planwerk UG – Visitenkarte</title>
<link href="https://fonts.googleapis.com/css2?family=Titillium+Web:wght@300;400&display=swap" rel="stylesheet">
<style>
  :root {
    --bg: #ececec;
    --card: #ffffff;
    --ink: #5d6c88;
    --ink-soft: #7a8699;
    --blue: #496ba0;
    --green: #9bc31d;
    --rule: #8a8f98;
  }
  * { box-sizing: border-box; margin: 0; padding: 0; }
  html, body { width: 977px; height: 1200px; overflow: hidden; }
  body {
    background: var(--bg);
    font-family: "Titillium Web", "Helvetica Neue", Arial, sans-serif;
    font-weight: 300;
    color: var(--ink);
    position: relative;
  }
  .card {
    position: absolute;
    left: 108px;
    width: 760px;
    height: 480px;
    background: var(--card);
    box-shadow: 0 6px 24px rgba(0,0,0,0.10);
    overflow: hidden;
  }
  .card--back { top: 95px; }
  .card--front { top: 625px; }

  /* Back side */
  .brand-large {
    position: absolute;
    left: 0; right: 0; top: 120px;
    text-align: center;
  }
  .brand-large .brand-mark {
    display: inline-block;
    width: 34px; height: 34px;
    background: var(--green);
    margin-bottom: 14px;
  }
  .brand-large .brand-name {
    font-size: 58px;
    line-height: 1.02;
    letter-spacing: 0.5px;
  }
  .legal {
    font-size: 9px;
    letter-spacing: 4px;
    color: var(--ink-soft);
    margin-top: 10px;
    font-weight: 400;
  }

  /* Front side */
  .bands { position: absolute; left: 0; top: 0; width: 760px; height: 90px; }
  .brand-small {
    position: absolute;
    left: 58px; top: 168px;
    width: 180px;
    text-align: center;
  }
  .brand-small .brand-mark {
    display: inline-block;
    width: 18px; height: 18px;
    background: var(--green);
    margin-bottom: 6px;
  }
  .brand-small .brand-name { font-size: 29px; line-height: 1.05; }
  .brand-small .legal { font-size: 5px; letter-spacing: 2px; margin-top: 5px; }
  .divider {
    position: absolute;
    left: 268px; top: 160px;
    width: 1px; height: 140px;
    background: var(--rule);
  }
  .person { position: absolute; left: 318px; top: 172px; }
  .person-name { font-size: 26px; letter-spacing: 0.5px; }
  .person-role { font-size: 17px; color: var(--ink-soft); margin-top: -4px; }

  .contact-row {
    position: absolute;
    left: 52px; right: 40px; top: 372px;
    display: flex;
    align-items: flex-end;
    gap: 54px;
    font-size: 15px;
    line-height: 1.35;
    color: var(--ink-soft);
  }
  .contact-block { display: grid; grid-template-columns: 16px auto; column-gap: 8px; align-items: center; }
  .address { display: block; }
  .icon { width: 13px; height: 13px; fill: #555b66; }
</style>
</head>
<body>

  <section class="card card--back" aria-label="Rückseite">
    <div class="brand-large">
      <span class="brand-mark"></span>
      <div class="brand-name">Taleron<br>Planwerk UG</div>
      <div class="legal">(HAFTUNGSBESCHRÄNKT)</div>
    </div>
  </section>

  <section class="card card--front" aria-label="Vorderseite">
    <svg class="bands" viewBox="0 0 760 90" aria-hidden="true">
      <polygon points="0,40 292,16 292,52 0,66" fill="var(--blue)"/>
      <polygon points="302,15 760,0 760,18 302,53" fill="var(--green)"/>
    </svg>

    <div class="brand-small">
      <span class="brand-mark"></span>
      <div class="brand-name">Taleron<br>Planwerk UG</div>
      <div class="legal">(HAFTUNGSBESCHRÄNKT)</div>
    </div>

    <div class="divider"></div>

    <div class="person">
      <div class="person-name">Jonas Mertens</div>
      <div class="person-role">Geschäftsführer</div>
    </div>

    <div class="contact-row">
      <div class="address">Ahornweg 18<br>04105 Leipzig</div>

      <div class="contact-block">
        <svg class="icon" viewBox="0 0 16 16" aria-hidden="true"><path d="M3.6 1.2l2.2 2.4-1.2 2a8.6 8.6 0 0 0 5.8 5.8l2-1.2 2.4 2.2-1.4 2.4C7.8 14.6 1.4 8.2 1.2 2.6z"/></svg>
        <span>+49 341 5550 2846</span>
        <svg class="icon" viewBox="0 0 16 16" aria-hidden="true"><rect x="4" y="1" width="8" height="5"/><rect x="1" y="6" width="14" height="7" rx="1"/><rect x="4" y="11" width="8" height="4" fill="#fff" stroke="#555b66" stroke-width="1"/></svg>
        <span>+49 341 5550 2840</span>
      </div>

      <div class="contact-block">
        <svg class="icon" viewBox="0 0 16 16" aria-hidden="true"><rect x="1" y="3" width="14" height="10"/><path d="M1 3l7 6 7-6" fill="none" stroke="#fff" stroke-width="1.4"/></svg>
        <span>info@taleron-planwerk.de</span>
        <svg class="icon" viewBox="0 0 16 16" aria-hidden="true"><g fill="none" stroke="#555b66" stroke-width="1.3"><circle cx="8" cy="8" r="6.5"/><ellipse cx="8" cy="8" rx="3" ry="6.5"/><path d="M1.5 8h13M2.5 4.8h11M2.5 11.2h11"/></g></svg>
        <span>www.taleron-planwerk.de</span>
      </div>
    </div>
  </section>

</body>
</html>
```